Business card with logo and words.

Colours: aqua and white (but open to suggestions).
Double sided card ok.
Need to convey competence, calmness, listening skills
Words:
Quiet Harbour Care Planning
Rhoda Pemberton
RN, RM, MVRNB, Grad Dip Gr & Pall Care Couns, Grad Cert Pall Care in Aged Care
quietharbourcp@fernmail.example

```html
<!DOCTYPE html>
<html lang="en">
<head>
<meta charset="utf-8">
<title>Quiet Harbour Care Planning – Business Card</title>
<link rel="stylesheet" href="https://fonts.googleapis.com/css2?family=Jost:wght@400;500&display=swap">
<style>
  :root {
    --aqua: #2aa9bf;
    --ocean: #1a6fae;
    --paper: #ffffff;
  }
  html, body {
    margin: 0;
    padding: 0;
    width: 1200px;
    height: 734px;
    overflow: hidden;
    background: var(--paper);
  }
  .card {
    position: relative;
    width: 1200px;
    height: 734px;
    background: var(--paper);
    font-family: "Jost", "Futura", sans-serif;
  }
  .practice-name {
    position: absolute;
    left: 38px;
    top: 124px;
    margin: 0;
    font-size: 43px;
    font-weight: 400;
    color: var(--aqua);
    letter-spacing: -0.2px;
  }
  .practitioner {
    position: absolute;
    left: 36px;
    top: 278px;
    margin: 0;
    font-size: 100px;
    font-weight: 500;
    color: var(--ocean);
    letter-spacing: -1px;
    line-height: 1;
  }
  .credentials {
    position: absolute;
    left: 40px;
    top: 430px;
    margin: 0;
    font-size: 20px;
    font-weight: 400;
    line-height: 31px;
    color: var(--ocean);
    text-transform: uppercase;
    letter-spacing: 0.3px;
  }
  .contact {
    position: absolute;
    left: 38px;
    top: 636px;
    margin: 0;
    font-size: 57px;
    font-weight: 400;
    color: var(--ocean);
    line-height: 1;
  }
  .brand-mark {
    position: absolute;
    left: 790px;
    top: 96px;
    display: flex;
    align-items: center;
    gap: 20px;
  }
  .brand-mark__dot {
    width: 96px;
    height: 96px;
    border-radius: 50%;
    background: var(--aqua);
    flex: none;
  }
  .brand-mark__name {
    font-size: 30px;
    font-weight: 400;
    color: var(--aqua);
    line-height: 1.15;
  }
</style>
</head>
<body>
  <div class="card">
    <div class="brand-mark">
      <span class="brand-mark__dot"></span>
      <span class="brand-mark__name">Quiet Harbour<br>Care Planning</span>
    </div>
    <p class="practice-name">Quiet Harbour Care Planning</p>
    <h1 class="practitioner">Rhoda Pemberton</h1>
    <p class="credentials">RN, RM, MVRNB, Grad Dip Gr &amp; Pall Care Couns,<br>Grad Cert Pall Care in Aged Care</p>
    <p class="contact">Email: quietharbourcp@fernmail.example</p>
  </div>
</body>
</html>
```